Business Card Design Project

i have the logo designed.
I require designs for the managing director and the general manager.
we need space for email, and a mobile number.
any other cool stuff/design you guys just let me see what you got.
The managing director card could be black, minimalist, and the cards for the rest of the company could be using the green logo.
it has to impress. transportation market is fragmented, we want to appear professional and sophisticated.
Md: Tarek bani rahim
General manager: omer rahim
clients: procurement heads of contracting companies
Business

```html
<!DOCTYPE html>
<html lang="en">
<head>
<meta charset="utf-8">
<title>Strideway Business Cards</title>
<link rel="stylesheet" href="https://fonts.googleapis.com/css2?family=Mulish:wght@400;700;800&display=swap">
<style>
:root{
  --stage:#ececec;
  --card:#ffffff;
  --ink:#262626;
  --black:#2b2a29;
  --green-dark:#147a3c;
  --green:#2f9a3a;
  --lime:#a8c92a;
  --white:#ffffff;
}
*{margin:0;padding:0;box-sizing:border-box}
html,body{width:1200px;height:773px;overflow:hidden;background:var(--stage)}
body{position:relative;font-family:"Mulish",Arial,sans-serif;color:var(--ink)}
.sprites{position:absolute;width:0;height:0}
.card-number{position:absolute;font-size:22px;font-weight:400;color:var(--ink)}
.card{position:absolute;width:525px;height:292px;background:var(--card);overflow:hidden;box-shadow:2px 4px 8px rgba(0,0,0,.22);border:1px solid #d8d8d8}
.card-art{position:absolute;inset:0;width:100%;height:100%}
.wordmark{position:absolute;font-weight:800;letter-spacing:.5px;line-height:1;white-space:nowrap}
.person{position:absolute;line-height:1;white-space:nowrap}
.person-name{font-size:22px;font-weight:700;letter-spacing:.3px}
.person-role{font-size:15px;font-weight:400;margin-top:8px}
.contacts{position:absolute;list-style:none;font-size:13px;font-weight:700;white-space:nowrap}
.contacts li{display:flex;align-items:center;gap:9px;height:23px}
.contacts svg{width:13px;height:13px;flex:none}
.web-strip{position:absolute;font-size:17px;font-weight:700;white-space:nowrap}
.icon{fill:none;stroke:var(--ink);stroke-width:1.3}
.on-dark{color:var(--white)}
.contacts.on-dark .icon{stroke:var(--white)}

/* card 1 */
.card-1{left:55px;top:52px}
.card-1 .wordmark{left:100px;top:130px;font-size:30px;color:var(--black)}
.card-1 .person{left:293px;top:64px}
.card-1 .contacts{left:293px;top:124px}
.card-1 .web-strip{left:172px;top:259px;color:var(--white)}

/* card 2 */
.card-2{left:634px;top:52px}
.card-2 .wordmark{left:200px;top:90px;font-size:32px;color:var(--black)}
.card-2 .person{left:57px;top:210px}
.card-2 .contacts{left:262px;top:184px}

/* card 3 */
.card-3{left:57px;top:424px}
.card-3 .wordmark{left:322px;top:140px;font-size:28px;color:var(--green)}
.card-3 .person{left:43px;top:66px}
.card-3 .contacts{left:43px;top:127px}
.card-3 .web-strip{left:40px;top:259px;color:var(--black)}

/* card 4 */
.card-4{left:632px;top:425px}
.card-4 .wordmark{left:192px;top:105px;font-size:36px;color:var(--green-dark)}
.card-4 .person{left:0;width:296px;text-align:center;top:208px}
.card-4 .contacts{left:275px;top:184px}
</style>
</head>
<body>

<svg class="sprites" aria-hidden="true">
  <symbol id="icon-phone" viewBox="0 0 14 14"><path d="M3 1.5l2.2 2.6-1.2 1.6c.8 1.7 2.2 3.1 3.9 3.9l1.6-1.2 2.6 2.2-1.4 1.9C6 12.3 1.7 8 1.1 2.9z"/></symbol>
  <symbol id="icon-mobile" viewBox="0 0 14 14"><rect x="3.5" y="1" width="7" height="12" rx="1.2"/><line x1="6" y1="11" x2="8" y2="11"/></symbol>
  <symbol id="icon-mail" viewBox="0 0 14 14"><rect x="1" y="3" width="12" height="8.5"/><path d="M1 3l6 5 6-5"/></symbol>
  <symbol id="icon-web" viewBox="0 0 14 14"><circle cx="7" cy="7" r="6"/><ellipse cx="7" cy="7" rx="2.6" ry="6"/><line x1="1" y1="7" x2="13" y2="7"/><line x1="2" y1="4" x2="12" y2="4"/><line x1="2" y1="10" x2="12" y2="10"/></symbol>
</svg>

<span class="card-number" style="left:30px;top:52px">1</span>
<span class="card-number" style="left:610px;top:56px">2</span>
<span class="card-number" style="left:35px;top:430px">3</span>
<span class="card-number" style="left:611px;top:426px">4</span>

<!-- Card 1: minimalist black -->
<section class="card card-1">
  <svg class="card-art" viewBox="0 0 525 292" preserveAspectRatio="none" aria-hidden="true">
    <path d="M0,228 C90,200 210,212 320,236 C420,256 480,240 525,212 L525,292 L0,292Z" fill="var(--black)"/>
    <path d="M0,250 C90,215 210,220 320,242 C410,258 470,250 525,226" fill="none" stroke="#fff" stroke-width="4"/>
  </svg>
  <div class="wordmark">Strideway</div>
  <div class="person">
    <div class="person-name">YOUR NAME</div>
    <div class="person-role">Managing Director</div>
  </div>
  <ul class="contacts">
    <li><svg class="icon"><use href="#icon-phone"/></svg>01 2345 6789</li>
    <li><svg class="icon"><use href="#icon-mobile"/></svg>00 0102 0102</li>
    <li><svg class="icon"><use href="#icon-mail"/></svg>email@strideway.com</li>
    <li><svg class="icon"><use href="#icon-web"/></svg>www.strideway.com</li>
  </ul>
  <div class="web-strip">www.strideway.com</div>
</section>

<!-- Card 2: black with green accents -->
<section class="card card-2">
  <svg class="card-art" viewBox="0 0 525 292" preserveAspectRatio="none" aria-hidden="true">
    <path d="M0,152 C130,132 260,140 370,162 C440,176 490,168 525,148 L525,292 L0,292Z" fill="var(--black)"/>
    <path d="M0,152 C40,144 100,138 165,142 C100,146 40,160 0,178Z" fill="var(--green)"/>
    <path d="M365,168 C440,172 495,160 525,134 L525,148 C490,168 440,176 365,168Z" fill="var(--green)"/>
  </svg>
  <div class="wordmark">Strideway</div>
  <div class="person on-dark">
    <div class="person-name">YOUR NAME</div>
    <div class="person-role">Managing Director</div>
  </div>
  <ul class="contacts on-dark">
    <li><svg class="icon"><use href="#icon-phone"/></svg>01 2345 6789</li>
    <li><svg class="icon"><use href="#icon-mobile"/></svg>00 0102 0102</li>
    <li><svg class="icon"><use href="#icon-mail"/></svg>email@strideway.com</li>
    <li><svg class="icon"><use href="#icon-web"/></svg>www.strideway.com</li>
  </ul>
</section>

<!-- Card 3: white with green band -->
<section class="card card-3">
  <svg class="card-art" viewBox="0 0 525 292" preserveAspectRatio="none" aria-hidden="true">
    <defs>
      <linearGradient id="band-lime" x1="0" x2="1">
        <stop offset="0" stop-color="var(--lime)"/><stop offset="1" stop-color="var(--green)"/>
      </linearGradient>
    </defs>
    <path d="M0,246 L222,246 L262,292 L0,292Z" fill="url(#band-lime)"/>
    <path d="M262,253 L525,253 L525,267 L278,267Z" fill="var(--black)"/>
    <path d="M250,274 L525,274 L525,292 L265,292Z" fill="var(--green)"/>
  </svg>
  <div class="wordmark">Strideway</div>
  <div class="person">
    <div class="person-name">YOUR NAME</div>
    <div class="person-role">General Manager</div>
  </div>
  <ul class="contacts">
    <li><svg class="icon"><use href="#icon-phone"/></svg>01 2345 6789</li>
    <li><svg class="icon"><use href="#icon-mobile"/></svg>00 0102 0102</li>
    <li><svg class="icon"><use href="#icon-mail"/></svg>email@strideway.com</li>
    <li><svg class="icon"><use href="#icon-web"/></svg>www.strideway.com</li>
  </ul>
  <div class="web-strip">www.strideway.com</div>
</section>

<!-- Card 4: green gradient -->
<section class="card card-4">
  <svg class="card-art" viewBox="0 0 525 292" preserveAspectRatio="none" aria-hidden="true">
    <defs>
      <linearGradient id="band-green" x1="0" x2="1">
        <stop offset="0" stop-color="var(--green-dark)"/><stop offset="1" stop-color="var(--lime)"/>
      </linearGradient>
    </defs>
    <rect x="0" y="158" width="525" height="134" fill="url(#band-green)"/>
    <line x1="237" y1="166" x2="237" y2="284" stroke="#fff" stroke-width="2" opacity=".85"/>
  </svg>
  <div class="wordmark">Strideway</div>
  <div class="person on-dark">
    <div class="person-name">YOUR NAME</div>
    <div class="person-role">Managing Director</div>
  </div>
  <ul class="contacts">
    <li><svg class="icon"><use href="#icon-phone"/></svg>01 2345 6789</li>
    <li><svg class="icon"><use href="#icon-mobile"/></svg>00 0102 0102</li>
    <li><svg class="icon"><use href="#icon-mail"/></svg>email@strideway.com</li>
    <li><svg class="icon"><use href="#icon-web"/></svg>www.strideway.com</li>
  </ul>
</section>

</body>
</html>
```